Horse related business entrepreneur needs a business card

I need a business card design for my horse related business. The enterprise is Copper Vale LLC and I have 3 businesses (headquartered at 2 locations): 1. property management where we rent horse stalls and apartments at a thoroughbred training center outside Ocala; 2. a medium sized transportation service in central Florida that sells horse bedding and removes used horse bedding from horse farms; and horse racing

```html
<!DOCTYPE html>
<html lang="en">
<head>
<meta charset="utf-8">
<title>Copper Vale LLC – Business Card</title>
<link href="https://fonts.googleapis.com/css2?family=Bitter:wght@400;600&family=Kaushan+Script&display=swap" rel="stylesheet">
<style>
  :root{
    --backdrop:#2a2a2b;
    --leather-light:#6a2a1a;
    --leather-mid:#4a1a12;
    --leather-dark:#260c09;
    --gold:#d4a543;
    --ink-light:#f3ece6;
    --shadow-tone:#2e0e0a;
  }
  *{box-sizing:border-box;margin:0;padding:0}
  html,body{width:1200px;height:900px;overflow:hidden;background:var(--backdrop)}
  .canvas{
    width:1200px;height:900px;display:flex;align-items:center;justify-content:center;gap:70px;
  }
  .card{
    position:relative;width:380px;height:664px;overflow:hidden;
    background:
      radial-gradient(ellipse 70% 55% at 50% 45%, var(--leather-light) 0%, var(--leather-mid) 55%, var(--leather-dark) 100%);
    box-shadow:0 20px 40px rgba(0,0,0,.55);
    font-family:"Bitter",Georgia,serif;color:var(--ink-light);
  }
  /* front */
  .brand{
    position:absolute;top:150px;left:0;right:0;display:flex;flex-direction:column;align-items:center;gap:16px;
  }
  .brand-dot{
    width:58px;height:58px;border-radius:50%;border:3px solid var(--gold);
  }
  .brand-name{
    font-weight:600;font-size:38px;letter-spacing:1px;color:var(--gold);text-transform:uppercase;
  }
  .holder{position:absolute;top:420px;left:0;right:0;text-align:center}
  .holder-name{font-family:"Kaushan Script",cursive;font-size:34px;line-height:1}
  .holder-role{font-size:15px;margin-top:4px}
  .contact{
    position:absolute;top:540px;left:0;right:0;text-align:center;font-size:18px;line-height:1.4;
  }
  /* back */
  .ornament{
    position:absolute;top:-20px;left:60px;width:300px;height:230px;border-radius:50%;
    background:radial-gradient(ellipse at center, rgba(46,14,10,.7), rgba(46,14,10,0) 70%);
  }
  .horse-figure{
    position:absolute;top:250px;left:150px;width:240px;height:300px;border-radius:45% 45% 30% 30%;
    background:radial-gradient(ellipse at 50% 40%, rgba(46,14,10,.75), rgba(46,14,10,0) 72%);
  }
  .addresses{
    position:absolute;top:205px;left:0;right:0;text-align:center;font-size:17px;line-height:1.35;
  }
  .addresses p + p{margin-top:18px}
</style>
</head>
<body>
<main class="canvas">
  <section class="card card-front">
    <div class="brand">
      <span class="brand-dot"></span>
      <span class="brand-name">Copper Vale LLC</span>
    </div>
    <div class="holder">
      <div class="holder-name">Wade Harlan</div>
      <div class="holder-role">Owner</div>
    </div>
    <div class="contact">
      <div>wade@coppervale.com</div>
      <div>p: (434) 555-0182</div>
      <div>f: (434) 555-0247</div>
    </div>
  </section>

  <section class="card card-back">
    <div class="ornament" role="img" aria-label="Faint swirl ornament"></div>
    <div class="horse-figure" role="img" aria-label="Faint rearing horse silhouette"></div>
    <div class="addresses">
      <p>1270 SE 92nd Terrace<br>Fairfield, FL 32686</p>
      <p>815 Willow Ridge Lane<br>Crozet, VA 22932</p>
    </div>
  </section>
</main>
</body>
</html>
```